a Label for a candle jar and its gift box

I would like a label that is modern minimalist for candles jars. These jars are colored as white, amber and black. I am thinking maybe foiling gold/silver background with logo only and maybe company name in different color that suits the foiling background color/s. I would like a high quality luxurious design that shows the preciousness of this candle. I am open to any ideas you might have for the design but so far I have used a logo only on the jar which I really like BUT I still feel that it is not enough branding for people when you only show them the logo so I am considering adding the business name. Again, I am open to both ideas (with logo only or logo with business name (Silken Meadow).

IMPORTANT: YOU MAY IGNORE MY DESIGN COMPLETELY AND DO YOUR OWN ONE AS LONG AS YOU KERP THE LOGO DESIGN. YOU MAY ALSO ADJUST THE LOGO A BIT TO SUIT YOUR DESIGN. - sorry im using capital letters to show importance but im not yelling :)

UPDATE: To clarify, I have uploaded a video called Corvel in the box to show what the current product look like. It is a corvel jar with a logo only and the jar box has a window that shows the jar with the logo on it and the back of that jar box has a bigger version of the label that has more details (i.e. Fragrance name and website link). So to make it clear, I would like to have two versions of the lables: 1. on the jar with minimal info (logo only or logo with the business name) 2. Bigger version of the label with more info to put on the back of the jar box - as described above. The dimensions of the jars are as per this link https://www.lunaxo-example.com.au/corvel-medium-base-and-flat-lid-amber-packed-with-lid-on/ The dimensions of the jar box as per this link https://www.lunaxo-example.com.au/corvel-medium-flat-lid-candle-box-with-window-beige/ Looking forward to some artistic productions :)

Update #2: Tues 25 Dec 18 1. I have uploaded the photo which has the logo with the name 'Silken Meadow' below it just for a reference. However, I would like the designer to modify the current font and NOT to use it as the word 'of in the phrase 'Silken Meadow' does not come out clear enough after printing. 2. I would like the designer NOT to create a design that will require a clear sticker/label for printing. 3. I have attached the photos of my current designs on the jars or the jar box just as a reference but please do NOT just use the same fonts and only change background. I am hoping to see something different and more professional than my own design :) Thank you very much!

Font styles to use
Decorative
Script

Requirements
Must have
• I would like them to fit on the three colors of the jars below - white, amber and black. Below is a link to how the jar looks like https://www.lunaxo-example.com.au/candle-making-supplies/candle-jars/corvel-candle-jars/?glassware_colour=415,443,417&glassware_size=268
Nice to have
• I would like to have a modern design which is suitable for both feminine and musculine.
Should not have
• shouldnt have so much writing on it!

```html
<!DOCTYPE html>
<html lang="en">
<head>
<meta charset="utf-8">
<title>Silken Meadow – Turkish Rose Candle Label</title>
<link rel="stylesheet" href="https://fonts.googleapis.com/css2?family=Marcellus&display=swap">
<style>
  :root {
    --paper: #ffffff;
    --ring: #3a3a3c;
    --sun: #fbbd12;
    --ink: #111111;
    --wreath-rose: #d98a98;
    --wreath-deep: #a3485c;
    --wreath-branch: #e8865a;
  }
  html, body {
    margin: 0;
    padding: 0;
    overflow: hidden;
    background: var(--paper);
  }
  .canvas {
    position: relative;
    width: 1181px;
    height: 1200px;
    overflow: hidden;
    background: var(--paper);
    font-family: "Marcellus", serif;
    color: var(--ink);
  }
  .label-art {
    position: absolute;
    inset: 0;
  }
  .label-text {
    position: absolute;
    left: 0;
    width: 1181px;
    margin: 0;
    text-align: center;
    white-space: nowrap;
    font-weight: 400;
    line-height: 1;
  }
  .brand-name {
    top: 428px;
    font-size: 76px;
    letter-spacing: 1px;
    text-transform: uppercase;
  }
  .product-line {
    top: 566px;
    font-size: 54px;
  }
  .tagline {
    top: 666px;
    font-size: 38px;
  }
  .scent-name {
    top: 762px;
    font-size: 66px;
  }
  .rule {
    position: absolute;
    left: 310px;
    width: 562px;
    height: 4px;
    background: var(--ink);
  }
  .rule-top { top: 648px; }
  .rule-bottom { top: 724px; }
</style>
</head>
<body>
<main class="canvas">
  <svg class="label-art" width="1181" height="1200" viewBox="0 0 1181 1200">
    <defs>
      <linearGradient id="wreathTone" x1="0" y1="0" x2="0" y2="1">
        <stop offset="0" stop-color="#e8865a" stop-opacity="0.55"/>
        <stop offset="0.6" stop-color="#d98a98" stop-opacity="0.75"/>
        <stop offset="1" stop-color="#a3485c" stop-opacity="0.85"/>
      </linearGradient>
    </defs>
    <circle class="outer-ring" cx="590" cy="600" r="532" fill="var(--ring)"/>
    <circle class="inner-disc" cx="590" cy="600" r="433" fill="var(--sun)"/>
    <g class="rose-wreath" role="img" aria-label="Illustrated wreath of pink roses, orange branches and lilac berry sprigs encircling the label">
      <circle cx="590" cy="600" r="440" fill="none" stroke="url(#wreathTone)" stroke-width="50"/>
    </g>
    <circle class="brand-mark" cx="580" cy="350" r="34" fill="none" stroke="var(--ink)" stroke-width="4"/>
  </svg>

  <h1 class="label-text brand-name">Silken Meadow</h1>
  <p class="label-text product-line">Natural Soy Wax Candles</p>
  <div class="rule rule-top"></div>
  <p class="label-text tagline">hand pournl with passion &amp; care</p>
  <div class="rule rule-bottom"></div>
  <p class="label-text scent-name">Turkish Rose</p>
</main>
</body>
</html>
```